Bramble Bites Society - A Monthly Subscription Dog Treats Club - Shopify Website Design

A monthly subscription company. Need a Shopify Website Design and uploaded to fully work with Tidewell Recurring.

Please look at these sites for examples as well as the images I enclosed.

https://www.platemarlo.example/
https://www.quirktastebox.example/

Number of Pages Required

1 page

```html
<!DOCTYPE html>
<html lang="en">
<head>
<meta charset="utf-8">
<title>Bramble Bites Society</title>
<link rel="stylesheet" href="https://fonts.googleapis.com/css2?family=Montserrat:wght@400;500;600;700;800&display=swap">
<style>
  :root {
    --hero-blue: #22a7f8;
    --ink: #111111;
    --text: #333333;
    --muted: #555555;
    --white: #ffffff;
    --rule: #8a8a8a;
    --card-bg: #f2f2f2;
    --card-line: #dddddd;
    --sale: #e5124b;
    --cream: #fbf6d3;
    --navy: #0b2a6b;
    --sky: #3ab4e6;
    --berry: #e31b3d;
  }
  * { box-sizing: border-box; margin: 0; padding: 0; }
  html, body { width: 1200px; height: 3652px; overflow: hidden; }
  body { position: relative; font-family: "Montserrat", sans-serif; color: var(--text); background: var(--white); }
  .abs { position: absolute; }

  /* Hero */
  .hero { position: absolute; left: 0; top: 0; width: 1200px; height: 790px; background: var(--hero-blue); }
  .brand { left: 143px; top: 44px; width: 260px; font-size: 27px; font-weight: 700; line-height: 34px; color: var(--navy); text-align: center; }
  .nav { left: 485px; top: 50px; display: flex; gap: 0; font-size: 15.5px; font-weight: 500; color: var(--ink); }
  .nav a { position: absolute; color: var(--ink); text-decoration: none; white-space: nowrap; top: 0; }
  .nav .current::after { content: ""; position: absolute; left: -2px; right: -2px; top: 30px; height: 3px; background: var(--ink); }
  .hero-photo { left: 10px; top: 150px; width: 680px; height: 600px; border-radius: 6px;
    background: linear-gradient(135deg, #c7a375 0%, #a8774a 45%, #6b3a1e 70%, #9aa7b5 100%); transform: rotate(-12deg); transform-origin: center; opacity: .95; }
  .hero-title { left: 706px; top: 305px; font-size: 52px; font-weight: 800; line-height: 62px; color: var(--white); letter-spacing: 1px; }
  .hero-sub { left: 706px; top: 455px; width: 380px; font-size: 20px; line-height: 31px; color: var(--white); }
  .btn-dark { background: var(--ink); color: var(--white); font-weight: 700; text-align: center; }
  .hero-btn { left: 706px; top: 550px; width: 135px; height: 36px; line-height: 36px; font-size: 14px; }
  .dot { width: 10px; height: 10px; border-radius: 50%; border: 2px solid var(--white); top: 727px; }
  .dot.on { background: var(--white); }

  /* Intro */
  .intro { left: 214px; top: 862px; width: 772px; font-size: 15.5px; line-height: 32.6px; color: var(--muted); text-align: center; }

  .section-title { left: 0; width: 1200px; text-align: center; font-size: 31px; font-weight: 700; color: var(--ink); letter-spacing: 1px; }
  .section-rule { left: 576px; width: 48px; height: 3px; background: var(--rule); }

  /* Posts */
  .post { display: flex; align-items: flex-end; justify-content: center; padding-bottom: 45px; }
  .post span { font-size: 20px; font-weight: 700; color: var(--white); letter-spacing: .5px; }
  .post-label { position: absolute; left: 0; width: 100%; text-align: center; font-size: 20px; font-weight: 700; color: var(--white); }

  /* Products */
  .product-card { background: var(--card-bg); border: 1px solid var(--card-line); }
  .product-shot { position: absolute; }
  .sale-badge { left: 468px; top: 2051px; width: 68px; height: 68px; border-radius: 50%; background: var(--sale); color: var(--white);
    font-size: 15px; font-weight: 600; line-height: 18px; text-align: center; padding-top: 16px; }
  .product-name { font-size: 15.5px; font-weight: 700; color: var(--ink); top: 2368px; }
  .product-price { font-size: 15.5px; color: var(--text); top: 2368px; text-align: right; width: 80px; }

  /* Spotlight */
  .spot-title { left: 655px; top: 2505px; font-size: 30px; font-weight: 700; color: var(--ink); letter-spacing: .5px; }
  .spot-desc { left: 656px; top: 2565px; font-size: 19px; color: var(--text); }
  .spot-price { left: 655px; top: 2622px; font-size: 30px; color: var(--ink); }
  .btn-outline { border: 1px solid #999; color: var(--ink); font-weight: 700; text-align: center; background: var(--white); }
  .spot-btn { top: 2689px; height: 50px; line-height: 48px; font-size: 19px; letter-spacing: .5px; }
  .full-details { left: 655px; top: 2808px; font-size: 19px; color: var(--ink); }
  .share { top: 2846px; display: flex; align-items: center; gap: 10px; font-size: 12px; }
  .share i { width: 30px; height: 30px; border-radius: 50%; display: block; }

  /* Newsletter */
  .newsletter { left: 0; top: 3004px; width: 1200px; height: 353px; background: var(--cream); }
  .nl-title { top: 3080px; font-size: 34px; letter-spacing: 1.5px; }
  .nl-sub { left: 0; top: 3140px; width: 1200px; text-align: center; font-size: 15.5px; color: var(--text); }
  .nl-field { left: 360px; top: 3232px; width: 477px; height: 46px; background: var(--white); border: 1px solid #e5e5e5; }
  .nl-placeholder { left: 382px; top: 3246px; font-size: 14px; color: #666; }
  .nl-btn { left: 732px; top: 3235px; width: 103px; height: 40px; line-height: 40px; font-size: 13px; }

  /* Footer */
  .foot-link { left: 172px; font-size: 16px; color: var(--text); }
  .social-ring { left: 437px; width: 42px; height: 42px; border-radius: 50%; border: 1.5px solid var(--ink); }
  .social-name { left: 498px; font-size: 16px; color: var(--text); }
  .copyright { left: 700px; width: 357px; top: 3418px; text-align: right; font-size: 15.5px; color: var(--text); }
  .pay { top: 3472px; width: 34px; height: 22px; border: 1px solid #ddd; border-radius: 3px; background: var(--white); }
  .pay i { position: absolute; left: 8px; top: 5px; width: 16px; height: 10px; border-radius: 2px; }
</style>
</head>
<body>

<header class="hero">
  <div class="abs hero-photo" role="img" aria-label="Open kraft box of braided yak chews on blue"></div>
  <div class="abs brand">Bramble Bites Society</div>
  <nav class="abs nav" style="left:0;top:50px;">
    <a class="current" style="left:485px">HOME</a>
    <a style="left:565px">ABOUT US</a>
    <a style="left:677px">PRODUCTS</a>
    <a style="left:795px">NEWS</a>
    <a style="left:874px">CONTACT</a>
  </nav>
  <svg class="abs" style="left:979px;top:52px" width="16" height="16" viewBox="0 0 16 16" aria-label="Search">
    <circle cx="6.5" cy="6.5" r="4.5" fill="none" stroke="#111" stroke-width="2.2"/>
    <line x1="10" y1="10" x2="14.5" y2="14.5" stroke="#111" stroke-width="2.4" stroke-linecap="round"/>
  </svg>
  <svg class="abs" style="left:1022px;top:47px" width="34" height="26" viewBox="0 0 34 26" aria-label="Cart">
    <path d="M2 3h5l4 14h16l4-10H9" fill="none" stroke="#111" stroke-width="2.4" stroke-linejoin="round"/>
    <circle cx="13" cy="22" r="2.3" fill="#111"/><circle cx="25" cy="22" r="2.3" fill="#111"/>
  </svg>

  <h1 class="abs hero-title">BRAMBLE BITES<br>SOCIETY</h1>
  <p class="abs hero-sub">At verosccusamus et iusto odio dignissimosloremippsy</p>
  <div class="abs btn-dark hero-btn">SHOP NOW</div>

  <svg class="abs" style="left:430px;top:724px" width="24" height="16" viewBox="0 0 24 16"><path d="M22 8H3M8 3L3 8l5 5" fill="none" stroke="#fff" stroke-width="2.2"/></svg>
  <div class="abs dot on" style="left:584px"></div>
  <div class="abs dot" style="left:602px"></div>
  <svg class="abs" style="left:746px;top:724px" width="24" height="16" viewBox="0 0 24 16"><path d="M2 8h19M16 3l5 5-5 5" fill="none" stroke="#fff" stroke-width="2.2"/></svg>
</header>

<p class="abs intro">Lorem ipsum dolor sit amet, consectetur adipiscing elit, sed do eiusmod tempor incididunt ut labore et dolore magna aliqua.nas accumsan lacus vel facilisirem ipsum dolor sit amet, consectetur adipiscing elit, sed do eiusmod tempor incididunt ut labore et dolore magna aliqua.nas accumsan lacus vel rem ipsum dolor sit amet, consectetur adipiscing elit, sed do eiusmod tempor incididunt</p>

<h2 class="abs section-title" style="top:1070px">FEATURED POSTS</h2>
<div class="abs section-rule" style="top:1137px"></div>

<div class="abs post" style="left:143px;top:1204px;width:450px;height:300px;background:linear-gradient(160deg,#c9a67a 0%,#4a3a36 55%,#1e1e24 100%)" role="img" aria-label="Box of dried yak chews"><span>LOREM IPSUM</span></div>
<div class="abs post" style="left:606px;top:1204px;width:449px;height:300px;background:linear-gradient(160deg,#5a2a1c 0%,#8c5a3a 50%,#b79e7f 100%)" role="img" aria-label="Box of bully sticks"><span>LABORE ET DOLOR</span></div>
<div class="abs post" style="left:143px;top:1516px;width:294px;height:300px;background:linear-gradient(160deg,#e8e2dc 0%,#b88276 50%,#4a3a38 100%)" role="img" aria-label="Gift boxes tied with ribbon"><span>SINT OCCAECAT</span></div>
<div class="abs post" style="left:452px;top:1516px;width:294px;height:300px;background:linear-gradient(160deg,#3a2a22 0%,#6b4a38 50%,#1c1a1c 100%)" role="img" aria-label="Divided tray of assorted jerky"><span>VOLUPTATEM</span></div>
<div class="abs post" style="left:760px;top:1516px;width:295px;height:300px;background:linear-gradient(170deg,#2bb2e0 0%,#7a5a42 40%,#5a3a2e 70%,#cfcfcf 100%)" role="img" aria-label="Open box of chopped treats"><span>NEMO ENIM</span></div>

<h2 class="abs section-title" style="top:1897px">FEATURED PRODUCTS</h2>
<div class="abs section-rule" style="top:1964px"></div>

<div class="abs product-card" style="left:142px;top:2031px;width:296px;height:309px"></div>
<div class="abs product-shot" style="left:170px;top:2105px;width:250px;height:160px;border-radius:6px;background:linear-gradient(160deg,#d2b48a 0%,#8a4a26 60%,#c9a47a 100%)" role="img" aria-label="Kraft box of braided chews"></div>
<div class="abs product-card" style="left:451px;top:2031px;width:296px;height:309px;background:linear-gradient(160deg,#7a4a32 0%,#4a2a20 50%,#b48c60 100%)" role="img" aria-label="Box of dried beef pieces"></div>
<div class="abs sale-badge">SAVE<br>$56</div>
<div class="abs product-card" style="left:760px;top:2031px;width:297px;height:309px"></div>
<div class="abs product-shot" style="left:790px;top:2080px;width:230px;height:180px;border-radius:6px;background:linear-gradient(150deg,#1e1e1e 0%,#e8707a 45%,#d9b27a 70%,#6bbf5a 100%)" role="img" aria-label="Gift box with bone shaped biscuits"></div>

<div class="abs product-name" style="left:157px">PRODUCT NAME</div>
<div class="abs product-price" style="left:343px">$56.87</div>
<div class="abs product-name" style="left:466px">PRODUCT NAME</div>
<div class="abs product-price" style="left:652px">$56.87</div>
<div class="abs product-name" style="left:775px">PRODUCT NAME</div>
<div class="abs product-price" style="left:961px">$56.87</div>

<div class="abs" style="left:143px;top:2485px;width:433px;height:420px;background:linear-gradient(150deg,#d9b98c 0%,#b07a4a 40%,#e0a0a8 70%,#8fc6dc 100%)" role="img" aria-label="Colourful boxes of assorted dog biscuits"></div>
<h3 class="abs spot-title">PRODUCT NAME</h3>
<p class="abs spot-desc">At vero eos et accusamus et iusto odi</p>
<div class="abs spot-price">$56.87</div>
<div class="abs btn-outline spot-btn" style="left:655px;width:173px">SHOP NOW</div>
<div class="abs btn-dark spot-btn" style="left:848px;width:171px">BUY IT NOW</div>
<div class="abs full-details">Full details &nbsp;<svg width="12" height="12" viewBox="0 0 12 12"><path d="M2 2l4 4-4 4M6 2l4 4-4 4" fill="none" stroke="#111" stroke-width="1.6"/></svg></div>
<div class="abs share" style="left:655px;color:var(--navy)"><i style="background:var(--navy)"></i>Share</div>
<div class="abs share" style="left:746px;color:var(--sky)"><i style="background:var(--sky)"></i>Post</div>
<div class="abs share" style="left:835px;color:var(--berry)"><i style="background:var(--berry)"></i>Pinboardly</div>

<section class="abs newsletter"></section>
<h2 class="abs section-title nl-title">SUBSCRIBE TO OUR NEWSLETTER</h2>
<p class="abs nl-sub">Sign up for our email list and get 15% off your first order</p>
<div class="abs section-rule" style="top:3186px"></div>
<div class="abs nl-field"></div>
<div class="abs nl-placeholder">Enter Email</div>
<div class="abs btn-dark nl-btn">SUBSCRIBE</div>

<footer>
  <div class="abs foot-link" style="top:3418px">Return Policy</div>
  <div class="abs foot-link" style="top:3457px">Search</div>
  <div class="abs foot-link" style="top:3495px">Blog</div>
  <div class="abs foot-link" style="top:3534px">Contact us</div>
  <div class="abs foot-link" style="top:3572px">About us</div>

  <div class="abs social-ring" style="top:3423px"></div>
  <div class="abs social-name" style="top:3434px">Circlebook</div>
  <div class="abs social-ring" style="top:3480px"></div>
  <div class="abs social-name" style="top:3491px">Chirpline</div>
  <div class="abs social-ring" style="top:3536px"></div>
  <div class="abs social-name" style="top:3547px">Lenscast</div>

  <div class="abs copyright">© 2020.Bramble Bites Society.All Rights Reserved</div>
  <div class="abs pay" style="left:726px"><i style="background:#1a2a7a"></i></div>
  <div class="abs pay" style="left:771px"><i style="background:#e8502a"></i></div>
  <div class="abs pay" style="left:816px"><i style="background:#2a7ad0"></i></div>
  <div class="abs pay" style="left:861px"><i style="background:#1a3a8a"></i></div>
  <div class="abs pay" style="left:906px"><i style="background:#3a6ac0"></i></div>
  <div class="abs pay" style="left:951px"><i style="background:#e89a2a"></i></div>
</footer>

</body>
</html>
```